item 1. 8.5x11 1-side flyer design
item 2. 18x24 1-side poster design (also wants at 8.5x11)
item 3. 11x8.5 2-side brochure
design with Larkfield Healthcare brand standards similar to the job you did under 360565
see all attachments

```html
<!DOCTYPE html>
<html lang="en">
<head>
<meta charset="utf-8">
<title>Syphilis FAQs Flyer</title>
<link href="https://fonts.googleapis.com/css2?family=Roboto:ital,wght@0,400;0,500;0,700;1,400&display=swap" rel="stylesheet">
<style>
  :root{
    --backdrop:#e4e4e4;
    --navy:#2e4453;
    --sage:#7c9d8b;
    --taupe:#a79e97;
    --ink:#2a3a46;
    --body:#333a40;
    --white:#ffffff;
  }
  *{margin:0;padding:0;box-sizing:border-box}
  html,body{width:1200px;height:1200px;overflow:hidden;background:var(--backdrop)}
  body{font-family:"Roboto",Arial,sans-serif;position:relative}
  .flyer{position:absolute;left:175px;top:271px;width:1368px;height:1058px;transform:scale(0.6213);transform-origin:0 0;overflow:hidden;background:var(--navy)}
  .scene-photo{position:absolute;inset:0;background:linear-gradient(160deg,#32495a 0%,#2d4352 55%,#3a5060 80%,#2c4150 100%)}
  .shapes{position:absolute;inset:0}
  .title{position:absolute;left:50px;top:62px;font-size:64px;font-weight:700;color:var(--taupe);letter-spacing:-1px}
  .photo-band{position:absolute;left:49px;top:137px;width:369px;height:12px;background:var(--taupe)}
  .photo{position:absolute;left:49px;top:149px;width:369px;height:438px;background:radial-gradient(ellipse at 55% 50%,#e7b7ad 0%,#f1dcd6 38%,#f4f2f1 70%,#eeeeee 100%)}
  .chart-title{position:absolute;left:60px;width:376px;top:648px;text-align:center;color:var(--white);font-size:17px;font-weight:500;line-height:22px}
  .chart-title .years{color:var(--sage);font-weight:400}
  .faq{position:absolute;width:360px}
  .faq .q{position:relative;font-size:21px;font-weight:500;color:var(--sage);line-height:28px;padding-left:35px;margin-left:-35px}
  .faq .q b{color:var(--ink);font-weight:700}
  .faq .q svg{position:absolute;left:0;top:1px;width:26px;height:26px}
  .faq p,.faq li{font-size:19.5px;color:var(--body);line-height:27.7px}
  .faq p b{color:var(--ink);font-weight:700}
  .faq p{margin-top:10px}
  .faq ul{list-style:none;margin-top:10px}
  .faq li::before{content:"• ";font-size:15px}
  .faq u{text-underline-offset:3px}
  .stat{position:absolute;top:850px;height:140px;text-align:center}
  .stat .frame{position:absolute;left:0;top:0}
  .stat .head{position:absolute;top:-10px;white-space:nowrap;color:var(--sage);line-height:60px}
  .stat .num{font-size:62px;font-weight:700}
  .stat .word{font-size:40px;font-weight:400;margin-left:16px}
  .stat .text{position:absolute;left:0;right:0;top:58px;color:var(--white);font-size:22px;line-height:31px;font-weight:500}
  .stat .text span{color:var(--sage);font-weight:400}
</style>
</head>
<body>
<div class="flyer">
  <div class="scene-photo" role="img" aria-label="Dimmed photo of a clinic interior"></div>
  <svg class="shapes" viewBox="0 0 1368 1058" width="1368" height="1058">
    <path d="M368,0 H1368 V605 C1230,720 1050,795 858,795 C640,795 470,700 410,560 C350,420 300,200 368,0 Z" fill="#ffffff"/>
  </svg>

  <div class="title">FAQs</div>
  <div class="photo-band"></div>
  <div class="photo" role="img" aria-label="Photo of hands with a red skin rash"></div>

  <div class="chart-title">Syphilis Cases in the United States<br><span class="years">1951-2021</span></div>
  <svg class="shapes" viewBox="0 0 1368 1058" width="1368" height="1058" font-family="Roboto, Arial, sans-serif">
    <g stroke="#ffffff" stroke-width="1" opacity="0.75">
      <line x1="111" y1="709" x2="111" y2="975"/><line x1="134" y1="709" x2="134" y2="975"/><line x1="157" y1="709" x2="157" y2="975"/><line x1="179" y1="709" x2="179" y2="975"/><line x1="202" y1="709" x2="202" y2="975"/><line x1="225" y1="709" x2="225" y2="975"/><line x1="248" y1="709" x2="248" y2="975"/><line x1="270" y1="709" x2="270" y2="975"/><line x1="293" y1="709" x2="293" y2="975"/><line x1="316" y1="709" x2="316" y2="975"/><line x1="339" y1="709" x2="339" y2="975"/><line x1="361" y1="709" x2="361" y2="975"/><line x1="384" y1="709" x2="384" y2="975"/><line x1="406" y1="709" x2="406" y2="975"/>
    </g>
    <g stroke="#ffffff" stroke-width="1.4">
      <line x1="88" y1="709" x2="88" y2="975"/><line x1="88" y1="975" x2="408" y2="975"/>
      <line x1="84" y1="709" x2="88" y2="709"/><line x1="84" y1="762" x2="88" y2="762"/><line x1="84" y1="815" x2="88" y2="815"/><line x1="84" y1="868" x2="88" y2="868"/><line x1="84" y1="921" x2="88" y2="921"/>
    </g>
    <g fill="#ffffff" font-size="8" text-anchor="end">
      <text x="82" y="712">200.000</text><text x="82" y="765">160.000</text><text x="82" y="818">120.000</text><text x="82" y="871">80.000</text><text x="82" y="924">40.000</text>
    </g>
    <g fill="#ffffff" font-size="8" text-anchor="middle">
      <text x="88" y="988">1951</text><text x="111" y="988">1956</text><text x="134" y="988">1961</text><text x="157" y="988">1966</text><text x="179" y="988">1971</text><text x="202" y="988">1976</text><text x="225" y="988">1981</text><text x="248" y="988">1986</text><text x="270" y="988">1991</text><text x="293" y="988">1996</text><text x="316" y="988">2001</text><text x="339" y="988">2006</text><text x="361" y="988">2011</text><text x="384" y="988">2016</text><text x="406" y="988">2021</text>
    </g>
    <text x="406" y="1008" fill="#ffffff" font-size="10" font-style="italic" text-anchor="end">Source HHDR</text>
    <polyline fill="none" stroke="#ffffff" stroke-width="3" stroke-linejoin="round" points="90,741 98,758 106,803 111,811 116,801 123,823 128,811 138,808 145,813 150,825 156,828 161,838 173,851 180,848 188,858 198,868 206,888 216,885 223,878 230,873 238,879 246,883 251,863 258,831 268,795 278,828 288,893 298,918 313,931 328,928 336,930 346,913 356,913 366,905 378,878 390,833 398,803 404,793 408,738"/>
  </svg>

  <div class="faq" style="left:528px;top:81px">
    <div class="q"><svg viewBox="0 0 26 26"><circle cx="13" cy="13" r="13" fill="#7c9d8b"/><text x="13" y="19" fill="#fff" font-size="17" font-weight="700" text-anchor="middle" font-family="Roboto, Arial, sans-serif">?</text></svg>What are the common <b>symptoms</b><br>of Syphilis?</div>
    <ul><li>Sores called chancres</li><li>Sore throat</li><li>Weight loss</li><li>Skin Rash</li><li>Joint pain</li><li>Fever</li><li>Fatigue</li></ul>
  </div>

  <div class="faq" style="left:528px;top:378px">
    <div class="q"><svg viewBox="0 0 26 26"><circle cx="13" cy="13" r="13" fill="#7c9d8b"/><text x="13" y="19" fill="#fff" font-size="17" font-weight="700" text-anchor="middle" font-family="Roboto, Arial, sans-serif">?</text></svg>How is Syphilis <b>diagnosed?</b></div>
    <p><b>Blood test</b> can determine if you have syphilis. Finger stick tests are&nbsp; available at some locations.</p>
  </div>

  <div class="faq" style="left:528px;top:536px">
    <div class="q"><svg viewBox="0 0 26 26"><circle cx="13" cy="13" r="13" fill="#7c9d8b"/><text x="13" y="19" fill="#fff" font-size="17" font-weight="700" text-anchor="middle" font-family="Roboto, Arial, sans-serif">?</text></svg>Can Syphilis be <b>treated?</b></div>
    <p><b>Yes.</b> Syphlis can be treated by<br>antibiotics commonly penicillin.</p>
  </div>

  <div class="faq" style="left:984px;top:81px;width:340px">
    <div class="q"><svg viewBox="0 0 26 26"><circle cx="13" cy="13" r="13" fill="#7c9d8b"/><text x="13" y="19" fill="#fff" font-size="17" font-weight="700" text-anchor="middle" font-family="Roboto, Arial, sans-serif">?</text></svg>What <b>causes</b> Syphilis?</div>
    <p>Syphilis is caused by a <b>bacteria</b> that is passed from person to person by sexual contact and blood transmission.</p>
  </div>

  <div class="faq" style="left:984px;top:267px;width:340px">
    <div class="q"><svg viewBox="0 0 26 26"><circle cx="13" cy="13" r="13" fill="#7c9d8b"/><text x="13" y="19" fill="#fff" font-size="17" font-weight="700" text-anchor="middle" font-family="Roboto, Arial, sans-serif">?</text></svg>What are the potential <b>health risks</b><br>associated with Syphilis?</div>
    <p>Without treatment syphilis remains in your system and can lead to <u>heart damage, brain damage, blindness, deafness, paralysis and death.</u> If a pregnant woman has it she can give it to the baby called <b>Congenital Syphilis.</b></p>
  </div>

  <div class="faq" style="left:984px;top:538px;width:300px">
    <div class="q"><svg viewBox="0 0 26 26"><circle cx="13" cy="13" r="13" fill="#7c9d8b"/><text x="13" y="19" fill="#fff" font-size="17" font-weight="700" text-anchor="middle" font-family="Roboto, Arial, sans-serif">?</text></svg>Can Syphilis affect <b>fertility?</b></div>
    <p><b>Yes.</b> Untreated syphilis can<br>cause infertility in both men and<br>women. It can also cause<br>miscarriages and<br>stillbirth.</p>
  </div>

  <div class="stat" style="left:493px;width:383px">
    <svg class="frame" width="383" height="140" viewBox="0 0 383 140"><path d="M173,1.5 H361.5 A20 20 0 0 1 381.5,21.5 V118.5 A20 20 0 0 1 361.5,138.5 H21.5 A20 20 0 0 1 1.5,118.5 V21.5 A20 20 0 0 1 21.5,1.5 H25" fill="none" stroke="#ffffff" stroke-width="3"/></svg>
    <div class="head" style="left:51px"><span class="num">80%</span><span class="word">Increase</span></div>
    <div class="text">Syphilis has risen 80% in the<br>United States from <span>2018-2022</span></div>
  </div>

  <div class="stat" style="left:949px;width:369px">
    <svg class="frame" width="369" height="140" viewBox="0 0 369 140"><path d="M187,1.5 H347.5 A20 20 0 0 1 367.5,21.5 V118.5 A20 20 0 0 1 347.5,138.5 H21.5 A20 20 0 0 1 1.5,118.5 V21.5 A20 20 0 0 1 21.5,1.5" fill="none" stroke="#ffffff" stroke-width="3"/></svg>
    <div class="head" style="left:28px"><span class="num">937%</span><span class="word">Increase</span></div>
    <div class="text" style="font-size:21px">Newborns born with syphilis has<br>increased 937% in the last <span>10 years</span></div>
  </div>
</div>
</body>
</html>
```